Cover needed for Tunevault/plimbra/digital release

Cover design needed for a Reggae song to be released as a single on tunevault/ disc mango/ plimbra/ vidhollow etc... for the artist it should say Marcus Delvane Meets Bluffmoors and the song: Sway Down Low Now. At the top it should say Marcus Delvane and (Meets Bluffmoors) can be in smaller letters. and the song title towards the bottom. Plus I would also like the same cover done without (Meets Bluffmoors) included in the picture. So in total 2 images. The image theme can be reggae/ dancehall/ rub a dub/ vinyl turntable related. Here is some information about the image quality that the website I am using wants it in:
1400 x 1400 pixels minimum; 3000 x 3000 pixels maximum
PNG, GIF, JPG, or JPEG file type
72 - 300dpi (300dpi is the best)
Less than 25mb
RGB color scheme (not CMYK)
Unique to this particular title. We cannot accept artwork that has been used for another title.
Uploaded image must match your physical album cover artwork.
IMPORTANT: If your artist name and the title of your album or single appear on your cover artwork, it MUST precisely match the information you provided for this project. The text should be identical. For instance, if the artist name you provided is "Pellow & Rundquist (featuring Varn & Bettick)," the text on your artwork should NOT say "Pellow and Rundquist."
Updates
I upgraded to be able to choose from more designs. Thank You
Target Market(s)
target market: Just Reggae fans dub fans, rub a dub/dancehall fans,

```html
<!DOCTYPE html>
<html lang="en">
<head>
<meta charset="utf-8">
<title>Marcus Delvane – Sway Down Low Now</title>
<link rel="stylesheet" href="https://fonts.googleapis.com/css2?family=Fredoka:wght@600;700&display=swap">
<style>
  :root {
    --cover-red: #c92024;
    --label-red: #c92024;
    --spindle-yellow: #fbdf0c;
    --text-white: #ffffff;
    --title-white: #f1f2f2;
    --green-deep: #1f6b3b;
    --green: #2b9a4b;
    --green-light: #5cb44f;
    --lime: #9cc73a;
    --yellow: #fbe00f;
    --amber: #f4c21f;
    --orange: #ec6d25;
    --red: #e31d24;
    --red-deep: #b81c20;
    --maroon: #5e0808;
  }
  html, body {
    margin: 0;
    padding: 0;
    overflow: hidden;
    background: var(--cover-red);
  }
  .cover {
    position: relative;
    width: 1200px;
    height: 1200px;
    background: var(--cover-red);
    overflow: hidden;
    font-family: "Fredoka", sans-serif;
  }
  .record {
    position: absolute;
    inset: 0;
    width: 1200px;
    height: 1200px;
  }
  .artist-name {
    position: absolute;
    top: 142px;
    left: 0;
    width: 1200px;
    margin: 0;
    text-align: center;
    font-weight: 700;
    font-size: 104px;
    line-height: 1.2;
    letter-spacing: 1px;
    text-transform: uppercase;
    color: var(--text-white);
  }
  .song-title {
    position: absolute;
    top: 970px;
    left: 0;
    width: 1200px;
    margin: 0;
    text-align: center;
    font-weight: 600;
    font-size: 70px;
    line-height: 1.2;
    letter-spacing: -0.5px;
    color: var(--title-white);
  }
</style>
</head>
<body>
  <main class="cover">
    <svg class="record" viewBox="0 0 1200 1200" aria-hidden="true">
      <defs>
        <linearGradient id="rasta-groove" x1="0" y1="0" x2="0" y2="1">
          <stop offset="0" stop-color="var(--green-deep)"/>
          <stop offset="0.14" stop-color="var(--green)"/>
          <stop offset="0.24" stop-color="var(--green-light)"/>
          <stop offset="0.31" stop-color="var(--lime)"/>
          <stop offset="0.37" stop-color="var(--yellow)"/>
          <stop offset="0.55" stop-color="var(--amber)"/>
          <stop offset="0.62" stop-color="#f0a526"/>
          <stop offset="0.69" stop-color="var(--orange)"/>
          <stop offset="0.75" stop-color="var(--red)"/>
          <stop offset="0.87" stop-color="var(--red-deep)"/>
          <stop offset="1" stop-color="var(--maroon)"/>
        </linearGradient>
      </defs>
      <circle class="record-disc" cx="600" cy="600" r="597" fill="url(#rasta-groove)"/>
      <circle class="record-label" cx="604" cy="588" r="248" fill="var(--label-red)"/>
      <circle class="record-spindle" cx="604" cy="584" r="17" fill="var(--spindle-yellow)"/>
    </svg>

    <h1 class="artist-name">Marcus Delvane</h1>
    <h2 class="song-title">Sway Down Low Now</h2>
  </main>
</body>
</html>
```